Veltrium stationery design

Design stationery for us that fits with the colours of the logo. We are looking for letterheads, business cards etc. Something we can use for a prospectus and marketing presentations in power point. Must be completed in such a manner that it represents a corporate image for large enterprise clients and other large organisations. The company is a project assurance and monitoring company that works in all industries.

```html
<!DOCTYPE html>
<html lang="en">
<head>
<meta charset="utf-8">
<title>Veltrium Business Card</title>
<link href="https://fonts.googleapis.com/css2?family=Montserrat:wght@400;500;700;800&display=swap" rel="stylesheet">
<style>
  :root {
    --navy: #0e1426;
    --navy-soft: #1a2134;
    --white: #ffffff;
    --red: #e8262b;
    --orange: #f4601f;
    --blue: #1f4f9e;
    --sky: #2f8fd6;
    --backdrop: #2b2b2d;
    --muted: #e6e8ef;
  }
  * { box-sizing: border-box; margin: 0; padding: 0; }
  html, body { width: 1200px; height: 900px; overflow: hidden; }
  body {
    background: var(--backdrop);
    font-family: "Montserrat", sans-serif;
    position: relative;
  }
  .card {
    position: absolute;
    left: 290px;
    width: 620px;
    height: 354px;
    border-radius: 22px;
    overflow: hidden;
  }
  .card--front { top: 70px; background: var(--navy); }
  .card--back {
    top: 484px;
    background: linear-gradient(135deg, var(--navy) 0%, var(--navy-soft) 55%, var(--navy) 100%);
    display: flex; align-items: center; justify-content: center;
  }
  .card__art { position: absolute; inset: 0; }
  .brand {
    display: flex; align-items: center; gap: 12px;
    font-weight: 800; letter-spacing: 2px;
  }
  .brand__dot { border-radius: 50%; background: var(--orange); flex: none; }
  .brand--front { position: absolute; top: 88px; right: 40px; color: var(--blue); font-size: 32px; }
  .brand--front .brand__dot { width: 32px; height: 32px; }
  .brand--back { color: var(--orange); font-size: 52px; }
  .brand--back .brand__dot { width: 52px; height: 52px; }
  .holder { position: absolute; left: 34px; top: 44px; color: var(--white); }
  .holder__name { font-size: 25px; font-weight: 800; letter-spacing: 0.5px; }
  .holder__first { color: var(--sky); }
  .holder__last { color: var(--red); }
  .holder__title { font-size: 13px; font-weight: 500; margin-top: 2px; color: var(--muted); }
  .contact { list-style: none; margin-top: 22px; font-size: 12.5px; color: var(--muted); }
  .contact li { display: flex; align-items: center; gap: 8px; margin-bottom: 6px; }
  .contact svg { width: 11px; height: 11px; flex: none; }
  .address {
    position: absolute; right: 40px; bottom: 20px;
    color: var(--white); font-size: 13px; line-height: 1.45; text-align: left;
  }
</style>
</head>
<body>

<section class="card card--front" aria-label="Business card front">
  <svg class="card__art" viewBox="0 0 620 354" aria-hidden="true">
    <path d="M170,0 C280,10 300,80 330,150 C365,240 430,262 620,262 L620,0 Z" fill="#ffffff"/>
    <path d="M170,0 C280,10 300,80 330,150 C365,240 430,262 640,262" fill="none" stroke="#e8262b" stroke-width="4" transform="translate(-6,7)"/>
    <path d="M170,0 C280,10 300,80 330,150 C365,240 430,262 640,262" fill="none" stroke="#1f4f9e" stroke-width="4" transform="translate(-12,13)"/>
    <path d="M170,0 C280,10 300,80 330,150 C365,240 430,262 640,262" fill="none" stroke="#f4601f" stroke-width="3" transform="translate(-18,19)"/>
  </svg>

  <div class="brand brand--front"><span class="brand__dot"></span>VELTRIUM</div>

  <div class="holder">
    <h1 class="holder__name"><span class="holder__first">DANA</span> <span class="holder__last">HOLLIS</span></h1>
    <p class="holder__title">Managing Director</p>
    <ul class="contact">
      <li><svg viewBox="0 0 12 12"><path d="M2 1 L4.5 1 L5.5 3.5 L4 4.5 Q5 7 7.5 8 L8.5 6.5 L11 7.5 L11 10 Q6 11 2.5 7 Q0.5 4 2 1 Z" fill="#e8262b"/></svg>123 456 789</li>
      <li><svg viewBox="0 0 12 12"><rect x="0.5" y="2" width="11" height="8" fill="#e8262b"/><path d="M0.5 2 L6 6.5 L11.5 2" fill="none" stroke="#0e1426" stroke-width="1"/></svg>info@veltrium.com</li>
      <li><svg viewBox="0 0 12 12"><circle cx="6" cy="6" r="5.5" fill="#e8262b"/><path d="M0.5 6 H11.5 M6 0.5 V11.5" stroke="#0e1426" stroke-width="0.8"/></svg>www.veltrium.com</li>
    </ul>
  </div>

  <p class="address">Your address,<br>City State, Zip 1234</p>
</section>

<section class="card card--back" aria-label="Business card back">
  <div class="brand brand--back"><span class="brand__dot"></span>VELTRIUM</div>
</section>

</body>
</html>
```